The Harvest Compass

Cutting Through the Noise to What Actually Works.

Nutrition book

Target Market(s)

People looking to be or get healthy and eat right.

```html
<!DOCTYPE html>
<html lang="en">
<head>
<meta charset="UTF-8">
<title>The Harvest Compass – Book Cover</title>
<link rel="stylesheet" href="https://fonts.googleapis.com/css2?family=Montserrat:wght@400;500;800;900&display=swap">
<style>
  :root {
    --page-bg: #efeae3;
    --cover-green: #2a9a38;
    --cover-green-light: #35ab42;
    --cover-green-dark: #1f8a2e;
    --title-white: #ffffff;
    --subtitle-yellow: #f3f7a6;
    --rule-color: rgba(255, 255, 255, 0.85);
    --crease: rgba(255, 255, 255, 0.18);
  }
  html, body {
    margin: 0;
    padding: 0;
    width: 1200px;
    height: 1200px;
    overflow: hidden;
    background: var(--page-bg);
  }
  .canvas {
    position: relative;
    width: 1200px;
    height: 1200px;
  }
  .book-cover {
    position: absolute;
    left: 190px;
    top: 40px;
    width: 820px;
    height: 1120px;
    background: var(--cover-green);
    overflow: hidden;
    font-family: "Montserrat", sans-serif;
    box-shadow: 0 10px 30px rgba(0, 0, 0, 0.15);
  }
  .food-doodle-pattern {
    position: absolute;
    inset: 0;
    background: radial-gradient(ellipse at 70% 20%, var(--cover-green-light), var(--cover-green) 55%, var(--cover-green-dark));
  }
  .spine-crease {
    position: absolute;
    top: 0;
    bottom: 0;
    left: 46px;
    width: 3px;
    background: var(--crease);
  }
  .cover-content {
    position: absolute;
    left: 118px;
    right: 60px;
    top: 120px;
  }
  .book-title {
    margin: 0;
    color: var(--title-white);
    font-weight: 800;
    font-size: 116px;
    line-height: 0.98;
    letter-spacing: -2px;
  }
  .book-subtitle {
    margin: 90px 0 0;
    color: var(--subtitle-yellow);
    font-weight: 800;
    font-size: 60px;
    line-height: 1.02;
    letter-spacing: -1px;
  }
  .book-tagline {
    margin: 30px 0 0;
    color: var(--title-white);
    font-weight: 500;
    font-size: 26px;
    line-height: 1.6;
    letter-spacing: 6px;
    text-transform: uppercase;
  }
  .author-rule {
    position: absolute;
    left: 118px;
    right: 90px;
    top: 965px;
    height: 2px;
    background: var(--rule-color);
  }
  .author-name {
    position: absolute;
    left: 118px;
    right: 90px;
    top: 1010px;
    margin: 0;
    text-align: center;
    color: var(--title-white);
    font-weight: 500;
    font-size: 22px;
    letter-spacing: 7px;
    text-transform: uppercase;
  }
</style>
</head>
<body>
  <main class="canvas">
    <section class="book-cover">
      <div class="food-doodle-pattern" role="img" aria-label="Faint line-drawn pattern of fruits, vegetables, cutlery, a muffin and a teacup"></div>
      <div class="spine-crease"></div>
      <div class="cover-content">
        <h1 class="book-title">The<br>Harvest<br>Compass</h1>
        <p class="book-subtitle">Cutting Through<br>the noise</p>
        <p class="book-tagline">To what<br>actually works.</p>
      </div>
      <div class="author-rule"></div>
      <p class="author-name">Your Name Here</p>
    </section>
  </main>
</body>
</html>
```